KVO-Business Card Design

I need a modern, professional business card design that includes my logo as the main feature, maybe the entire background with the contact info overlaying or even contact info on the back and the logo full frontal

Neat and organized placement of contact information

Would like to see options in black and white

Target Market(s)

real estate Developers, Construction managers, business and home owners

Industry/Entity Type

Construction

Contact Information for Business Card

KVO Construction
Danny Ferrante
General Contractor

Office: 1-888-902-7315 Ext #1
Cell: 215-730-4162
Fax: 1-888-902-7315

Font styles to use
Serif

Requirements
Must have
• title
• office #
• cell #
• Email
• website
Nice to have
• fax

```html
<!DOCTYPE html>
<html lang="en">
<head>
<meta charset="utf-8">
<title>KVO Construction – Business Card</title>
<link rel="stylesheet" href="https://fonts.googleapis.com/css2?family=Roboto+Slab:wght@400;700;800&display=swap">
<style>
  :root {
    --page: #ffffff;
    --card: #000000;
    --green: #2e7544;
    --white: #ffffff;
  }
  html, body {
    margin: 0;
    padding: 0;
    width: 1200px;
    height: 703px;
    overflow: hidden;
    background: var(--page);
    font-family: "Roboto Slab", serif;
  }
  .canvas { position: relative; width: 1200px; height: 703px; }
  .card {
    position: absolute; left: 23px; top: 23px;
    width: 1152px; height: 589px;
    background: var(--card);
  }
  .base-band {
    position: absolute; left: 262px; top: 612px;
    width: 691px; height: 66px;
    background: var(--green);
  }
  .brand-mark {
    position: absolute; left: 40px; top: 78px;
    width: 160px; height: 104px;
    display: flex; align-items: center; justify-content: center;
    color: var(--green); font-weight: 800; font-size: 60px; line-height: 1;
  }
  .brand-divider {
    position: absolute; left: 212px; top: 82px;
    width: 4px; height: 113px; background: var(--white);
  }
  .company-name {
    position: absolute; left: 233px; top: 117px;
    margin: 0; color: var(--white);
    font-size: 39px; font-weight: 700; line-height: 1;
  }
  .person {
    position: absolute; right: 85px; top: 100px;
    text-align: right;
  }
  .person-name {
    margin: 0; color: var(--green);
    font-size: 36px; font-weight: 700; line-height: 1;
  }
  .person-title {
    margin: 6px 0 0; color: var(--white);
    font-size: 28px; font-weight: 400; line-height: 1.1;
  }
  .accent-green {
    position: absolute; left: 1133px; top: 83px;
    width: 13px; height: 112px; background: var(--green);
  }
  .accent-white {
    position: absolute; left: 1146px; top: 83px;
    width: 27px; height: 112px; background: var(--white);
  }
  .rule {
    position: absolute; left: 60px; top: 351px;
    width: 1085px; height: 4px; background: var(--white);
  }
  .detail {
    position: absolute;
    color: var(--green); font-size: 23px; font-weight: 700; line-height: 32px;
  }
  .office-address { left: 61px; top: 476px; }
  .website { left: 61px; top: 547px; }
  .contact { right: 123px; text-align: right; }
  .contact-phone { top: 387px; }
  .contact-fax { top: 476px; }
  .contact-email { top: 547px; }
  .icon { position: absolute; fill: var(--white); }
</style>
</head>
<body>
<div class="canvas">
  <div class="base-band"></div>
  <div class="card"></div>

  <div class="brand-mark">KVO</div>
  <div class="brand-divider"></div>
  <h1 class="company-name">KVO Construction</h1>

  <div class="person">
    <p class="person-name">DANNY FERRANTE</p>
    <p class="person-title">General Contractor</p>
  </div>
  <div class="accent-green"></div>
  <div class="accent-white"></div>

  <div class="rule"></div>

  <div class="detail office-address">Office address</div>
  <div class="detail website">www.kvoconstruction.com</div>

  <div class="detail contact contact-phone">1-888-902-7315&nbsp;&nbsp;Ext#1<br>215-730-4162</div>
  <svg class="icon icon-phone" style="left:1090px;top:391px" width="46" height="44" viewBox="0 0 24 24" aria-hidden="true">
    <path d="M6.6 2.2c.5-.3 1.1-.2 1.4.3l2.3 3.6c.3.5.2 1.1-.2 1.4L8.6 8.7c.9 2.4 2.9 4.6 5.3 5.8l1.2-1.4c.4-.4 1-.5 1.5-.2l3.6 2.3c.5.3.6 1 .3 1.4l-1.4 2.4c-.5.8-1.4 1.2-2.3 1-7.3-1.8-12.3-7.2-13.6-13.8-.2-.9.2-1.8 1-2.2z"/>
  </svg>

  <div class="detail contact contact-fax">1-888-902-7315</div>
  <svg class="icon icon-fax" style="left:1092px;top:468px" width="50" height="50" viewBox="0 0 24 24" aria-hidden="true">
    <path d="M6 2h9l3 3v4h-2V5.8L14.2 4H8v5H6z"/>
    <path d="M3 10h18a1 1 0 0 1 1 1v7h-4v-2h2v-4H4v4h2v2H2v-7a1 1 0 0 1 1-1z"/>
    <path d="M6 14h12v8H6zm2 2v4h8v-4z"/>
  </svg>

  <div class="detail contact contact-email">email@email.com</div>
  <svg class="icon icon-mail" style="left:1096px;top:550px" width="45" height="34" viewBox="0 0 26 20" aria-hidden="true">
    <path d="M1 1h24v18H1zm2 2v.4l10 8 10-8V3zm20 2.9-6.4 5.1L23 16.6zM3 5.9v10.7l6.4-5.6zm7.9 6.3L3 17h20l-7.9-4.8L13 14z"/>
  </svg>
</div>
</body>
</html>
```